QOR Infographic Design and Business Card design

We have an infographic but it could use some updating and creativity applied to it. Would like to match it a bit more to our current logo and web design (although it doesn’t have to match per se, thinking of updating it too) http://qor-advisory.example/QOR_Advisory/QOR_Advisory___Your_treasury_pricing_and_fee_negotiation_specialists.html
Can be double sided

Target Market(s)

Companies that make more than $150MM a year

Industry/Entity Type

Business

Contact Information for Business Card

Uploaded the logo and you can also look at the website.

Font styles to use
Sans Serif

Requirements
Must have
• Must look professional. Looking to stick to the same colors in the logo, the logo won’t change. Very open after that
Nice to have
• Front and back on the card

```html
<!DOCTYPE html>
<html lang="en">
<head>
<meta charset="utf-8">
<title>QOR Advisory – Business Card</title>
<link rel="stylesheet" href="https://fonts.googleapis.com/css2?family=Open+Sans:wght@400;600;700&display=swap">
<style>
  :root {
    --bg: #e9e6e1;
    --card: #ffffff;
    --brand-red: #b3261e;
    --brand-red-dark: #8f1b15;
    --ink: #555555;
    --ink-soft: #7a7a7a;
    --white: #ffffff;
  }
  * { box-sizing: border-box; margin: 0; padding: 0; }
  html, body { width: 1200px; height: 950px; overflow: hidden; }
  body {
    background: var(--bg);
    font-family: "Open Sans", Arial, sans-serif;
    position: relative;
  }
  .card {
    position: absolute;
    left: 240px;
    width: 720px;
    height: 411px;
    background: var(--card);
    box-shadow: 0 6px 18px rgba(0,0,0,0.18);
    overflow: hidden;
  }
  .card--front { top: 46px; }
  .card--back { top: 493px; }

  .brand {
    display: flex;
    flex-direction: column;
    align-items: flex-start;
  }
  .brand__row { display: flex; align-items: center; gap: 12px; }
  .brand__dot {
    width: 40px; height: 40px;
    border-radius: 50%;
    border: 6px solid var(--brand-red);
  }
  .brand__name {
    font-weight: 700;
    font-size: 52px;
    letter-spacing: 6px;
    color: var(--ink);
    line-height: 1;
  }
  .brand__domain {
    font-weight: 700;
    font-size: 22px;
    color: var(--ink-soft);
    margin-top: 8px;
  }

  .card--front .brand {
    position: absolute;
    left: 50%; top: 50%;
    transform: translate(-50%, -50%);
  }

  .card--back .band {
    position: absolute;
    left: 0; top: 140px;
    width: 470px; height: 96px;
    background: linear-gradient(90deg, var(--brand-red-dark), var(--brand-red));
    border-radius: 0 48px 48px 0;
    padding: 20px 0 0 48px;
    color: var(--white);
  }
  .holder__name { font-weight: 700; font-size: 26px; line-height: 1.15; }
  .holder__role { font-size: 16px; }

  .card--back .brand {
    position: absolute;
    left: 490px; top: 130px;
  }
  .card--back .brand__name { font-size: 44px; }
  .card--back .brand__dot { width: 34px; height: 34px; border-width: 5px; }
  .card--back .brand__domain { font-size: 18px; }

  .contact {
    position: absolute;
    left: 48px; top: 282px;
    color: var(--ink-soft);
    font-size: 16px;
    line-height: 1.45;
    list-style: none;
  }
  .contact__line { display: flex; align-items: center; gap: 8px; }
  .contact__icon { width: 16px; height: 16px; fill: var(--brand-red); }
  .contact__gap { height: 6px; }
</style>
</head>
<body>
  <section class="card card--front" aria-label="Card front">
    <div class="brand">
      <div class="brand__row">
        <span class="brand__dot" aria-hidden="true"></span>
        <span class="brand__name">QOR</span>
      </div>
      <span class="brand__domain">QOR-Advisory.example</span>
    </div>
  </section>

  <section class="card card--back" aria-label="Card back">
    <div class="band">
      <p class="holder__name">Daniel Reyes</p>
      <p class="holder__role">CEO/Founder</p>
    </div>
    <div class="brand">
      <div class="brand__row">
        <span class="brand__dot" aria-hidden="true"></span>
        <span class="brand__name">QOR</span>
      </div>
      <span class="brand__domain">QOR-Advisory.example</span>
    </div>
    <ul class="contact">
      <li class="contact__line">4120 Birchwood Court</li>
      <li class="contact__line">Juneau, Alaska 99801</li>
      <li class="contact__gap" aria-hidden="true"></li>
      <li class="contact__line">
        <svg class="contact__icon" viewBox="0 0 16 16" aria-hidden="true"><path d="M3.5 1.5l2.5 2.7-1.4 1.8c.8 1.9 2.3 3.4 4.2 4.2l1.8-1.4 2.7 2.5-1.5 2.2C6.9 13.2 2.8 9.1 1.3 3z"/></svg>
        555 014 2290
      </li>
      <li class="contact__line">
        <svg class="contact__icon" viewBox="0 0 16 16" aria-hidden="true"><path d="M1 3.5h14v9H1z M1.5 4l6.5 5 6.5-5" fill="var(--brand-red)"/><path d="M1.8 4.2L8 8.8l6.2-4.6" fill="none" stroke="#fff" stroke-width="1.2"/></svg>
        hello@qor-advisory.example
      </li>
    </ul>
  </section>
</body>
</html>
```